Business needs Office Posters Designed

I need a office poster designed to put on a 2 feet x 3 feet space:
My Employee is Better Than Me.
- to signify the importance of listening to your employees, because they know better, more experienced in their respective fields.

Target Market(s)

employees

Industry/Entity Type

Healthcare

```html
<!DOCTYPE html>
<html lang="en">
<head>
<meta charset="UTF-8">
<title>Listen to Your Staff – Office Poster</title>
<link href="https://fonts.googleapis.com/css2?family=Questrial&display=swap" rel="stylesheet">
<style>
  :root {
    --navy: #0b0d2e;
    --maroon: #7a1a35;
    --white: #ffffff;
    --accent-blue: #b9d4e6;
    --photo-light: #c9ccd0;
    --photo-mid: #8a8f96;
    --photo-dark: #3a3d45;
    --page-bg: #ffffff;
  }
  * { margin: 0; padding: 0; box-sizing: border-box; }
  html, body {
    width: 942px;
    height: 1200px;
    overflow: hidden;
    background: var(--page-bg);
  }
  .poster {
    position: relative;
    width: 942px;
    height: 1200px;
    overflow: hidden;
    background: var(--navy);
    font-family: "Questrial", sans-serif;
  }
  .poster__photo {
    position: absolute;
    left: 0;
    top: 0;
    width: 942px;
    height: 770px;
    background: linear-gradient(100deg,
      var(--photo-dark) 0%,
      var(--photo-mid) 30%,
      var(--photo-light) 55%,
      var(--photo-mid) 80%,
      var(--photo-dark) 100%);
  }
  .poster__chevron {
    position: absolute;
    left: 0;
    top: 0;
    width: 942px;
    height: 1200px;
  }
  .chevron__band { fill: var(--maroon); }
  .chevron__panel { fill: var(--navy); }
  .poster__message {
    position: absolute;
    left: 0;
    top: 785px;
    width: 942px;
    text-align: center;
    color: var(--white);
  }
  .message__lead {
    font-size: 57px;
    line-height: 73px;
    letter-spacing: 0.2px;
  }
  .message__call {
    display: block;
    margin-top: 14px;
    padding-left: 40px;
    color: var(--accent-blue);
    font-size: 44px;
    letter-spacing: 1.5px;
    text-transform: uppercase;
    -webkit-text-stroke: 1px var(--accent-blue);
  }
  .message__call .dot { color: var(--white); -webkit-text-stroke: 1px var(--white); }
</style>
</head>
<body>
  <main class="poster">
    <div class="poster__photo" role="img" aria-label="Photo of a manager leaning over a glass desk, listening to a female employee who points at documents in an office"></div>

    <svg class="poster__chevron" viewBox="0 0 942 1200" aria-hidden="true">
      <polygon class="chevron__band" points="0,700 471,612 942,700 942,762 471,662 0,762"/>
      <polygon class="chevron__panel" points="0,762 471,662 942,762 942,1200 0,1200"/>
    </svg>

    <section class="poster__message">
      <p class="message__lead">Ask your staff how they<br>would do their job if it<br>were up to them</p>
      <p class="message__call">- And then listen<span class="dot">.</span></p>
    </section>
  </main>
</body>
</html>
```